Business Card Design for Event Planning Company

Create a business card for event planning company using our new logo. After I pick the design, I will need files made for 6 employees. Our company provides event design & logistics services as well as venue management. The font should be sans serif and complementary to the logo. I will need to know the name of the font selected for the final design. The phone numbers listed should be separated by "." not "-"

Address for the card
PO Box 318, Washington, DC 20019

Card One
Lorna Pettibone
lpettibone@galavoyant.com
202.481.7730

Card Two
Miriam Okonkwo
mokonkwo@galavoyant.com
202.556.2047

Card Three
Tessa Varnholt
tvarnholt@galavoyant.com
978.620.4471

Card Four
Robin Fess
rfess@galavoyant.com
202.718.3362

Card Five
Ada-Rose Pelletan-Uzor
adarose@galavoyant.com
202.839.1205

Card Six
Beatrix Holloway
Beatrix@galavoyant.com
202.492.6618

Target Market(s)

Corporate/Non-Profit

Industry/Entity Type

Event Planning

Contact Information for Business Card

Address for the card

Card One
Lorna Pettibone
lpettibone@galavoyant.com
202.481.7730

Card Two
Miriam Okonkwo
202.556.2047

Card Three
Tessa Varnholt
978.620.4471

Card Four
Robin Fess
rfess@galavoyant.com
202.718.3362

Card Five
Ada-Rose Pelletan-Uzor
202.839.1205

Card Six
Beatrix Holloway
202.492.6618

Font styles to use
Sans Serif

Colors

Designer to choose colors to be used in the design.

Requirements
Must have
• Two-sided with logo
Should not have
• Extra colors or be too busy

```html
<!DOCTYPE html>
<html lang="en">
<head>
<meta charset="utf-8">
<title>Galavoyant Business Card</title>
<link rel="stylesheet" href="https://fonts.googleapis.com/css2?family=Arimo:wght@400;700&display=swap">
<style>
  :root {
    --backdrop: #4b433e;
    --card: #151617;
    --teal: #5aa7a6;
    --white: #f4f4f4;
    --muted: #7b7c7e;
    --rule: #9a9b9d;
  }
  * { margin: 0; padding: 0; box-sizing: border-box; }
  html, body {
    width: 1200px;
    height: 864px;
    overflow: hidden;
    background: var(--backdrop);
    font-family: "Arimo", Arial, sans-serif;
  }
  .canvas {
    width: 1200px;
    height: 864px;
    display: flex;
    align-items: center;
    justify-content: center;
    gap: 40px;
  }
  .card {
    width: 540px;
    height: 309px;
    background: var(--card);
    position: relative;
    box-shadow: 0 14px 30px rgba(0,0,0,0.45);
  }
  /* Back side */
  .card-back {
    display: flex;
    flex-direction: column;
    align-items: center;
    justify-content: center;
  }
  .card-back .wordmark {
    font-size: 50px;
    font-weight: 400;
    color: var(--muted);
    letter-spacing: 0.5px;
  }
  .card-back .website {
    margin-top: 22px;
    font-size: 12px;
    color: var(--muted);
    letter-spacing: 6px;
  }
  /* Front side */
  .card-front {
    display: flex;
    align-items: center;
  }
  .brand-mark {
    width: 230px;
    display: flex;
    align-items: center;
    justify-content: center;
    gap: 10px;
  }
  .brand-mark .dot {
    width: 14px;
    height: 14px;
    border-radius: 50%;
    background: var(--teal);
  }
  .brand-mark .wordmark {
    font-size: 32px;
    font-weight: 400;
    color: var(--teal);
  }
  .divider {
    width: 1px;
    height: 150px;
    background: var(--rule);
    margin-right: 26px;
  }
  .contact {
    color: var(--white);
    font-size: 14px;
    line-height: 1.3;
  }
  .contact .person {
    color: var(--teal);
    font-weight: 700;
    font-size: 18px;
    letter-spacing: 1px;
    text-transform: uppercase;
    margin-bottom: 8px;
  }
  .contact .address { margin-bottom: 8px; }
  .contact .line {
    display: flex;
    align-items: center;
    gap: 10px;
  }
  .contact .line svg {
    width: 12px;
    height: 12px;
    flex: none;
    fill: var(--teal);
  }
</style>
</head>
<body>
<main class="canvas">
  <section class="card card-back" aria-label="Card back">
    <div class="wordmark">galavoyant</div>
    <div class="website">www.galavoyant.com</div>
  </section>

  <section class="card card-front" aria-label="Card front">
    <div class="brand-mark">
      <span class="dot"></span>
      <span class="wordmark">galavoyant</span>
    </div>
    <div class="divider"></div>
    <div class="contact">
      <div class="person">Lorna Pettibone</div>
      <div class="address">PO Box 318, Washington,<br>DC 20019</div>
      <div class="line">
        <svg viewBox="0 0 12 12" aria-hidden="true"><path d="M3 0h6a1 1 0 0 1 1 1v10a1 1 0 0 1-1 1H3a1 1 0 0 1-1-1V1a1 1 0 0 1 1-1zm0 2v7h6V2z"/></svg>
        <span>202.481.7730</span>
      </div>
      <div class="line">
        <svg viewBox="0 0 12 12" aria-hidden="true"><path d="M0 2h12v1L6 7 0 3z M0 4.5l6 4 6-4V10H0z"/></svg>
        <span>lpettibone@galavoyant.com</span>
      </div>
      <div class="line">
        <svg viewBox="0 0 12 12" aria-hidden="true"><circle cx="6" cy="6" r="6"/><path d="M1 6h10M6 1v10" stroke="#151617" stroke-width="1"/></svg>
        <span>www.galavoyant.com</span>
      </div>
    </div>
  </section>
</main>
</body>
</html>
```